BrivoMatex. Lantern for the Steady Growth. Business card

Professional business card for BrivoMatex (Lantern for the Steady Growth)
My rationale: Strategy-> Execution-> Results-> Value that lead to the BrivoMatex name: We put the Lantern for the Steady Growth.
We deliver value to our customers helping them at defining a good strategy (cyan arrow). 90% of well formulated strategies fail due to poor execution so we also consider strategical execution very important (green arrow). Due to the execution we obtain the results (blue arrow). Finally, the results provide feedback to redefine strategy, and the new strategy has to be executed and new results obtained providing new feedback and on and on. It's like a wheel that finally, must create corporate value: value for shareholders, staholders, employees, providers...-

Target Market(s)

CEOs and steering comitees , invewrnent funds

Industry/Entity Type

Business Consultant

Contact Information for Business Card

Tommaso Ferlini
CEO & Founder
tommaso.ferlini@brivomatex.example
Mobile: +34 611.205.938
www.brivomatex.example

Colors

Designer to choose colors to be used in the design.

Requirements
Nice to have
• Nice to hace the words: Strategy, execution, results
• Nice to vave the claim: Lantern for the Steady Growth
• The three colors should be shown:
• cyan for STRATEGY
• green for EXECUTION
• blue for RESULTS
Should not have
• Complete black background

```html
<!DOCTYPE html>
<html lang="en">
<head>
<meta charset="utf-8">
<title>BrivoMatex — Business Card</title>
<link rel="stylesheet" href="https://fonts.googleapis.com/css2?family=Montserrat:wght@400;500;600;700&display=swap">
<style>
  :root {
    --backdrop: #3b322e;
    --card: #1b1b1d;
    --card-edge: #1d8fc4;
    --ink: #f4f4f4;
    --ink-soft: #d9d9d9;
    --cyan: #1fa9e6;
    --green: #8dc641;
    --blue: #1479b8;
  }
  * { box-sizing: border-box; margin: 0; padding: 0; }
  html, body {
    width: 1200px; height: 716px; overflow: hidden;
    background: var(--backdrop);
    font-family: "Montserrat", sans-serif;
  }
  .stage {
    width: 1200px; height: 716px;
    display: flex; align-items: center; justify-content: center; gap: 48px;
  }
  .card {
    width: 540px; height: 309px;
    background: var(--card);
    border-radius: 6px;
    position: relative;
    box-shadow: 0 10px 24px rgba(0,0,0,.45);
  }
  .card--front { box-shadow: 0 4px 0 var(--card-edge), 0 14px 26px rgba(0,0,0,.45); }
  .brand {
    display: flex; align-items: center; gap: 10px;
    color: var(--ink); font-weight: 700; letter-spacing: -0.5px;
  }
  .brand__dot { width: 14px; height: 14px; border-radius: 50%; background: var(--cyan); flex: none; }
  .card--front .brand {
    position: absolute; left: 50%; top: 50%; transform: translate(-50%, -50%);
    font-size: 44px;
  }
  .card--back { display: flex; align-items: center; padding: 0 34px; }
  .card--back .brand { font-size: 30px; flex: none; }
  .divider { width: 2px; height: 130px; background: var(--green); margin: 0 22px; flex: none; }
  .contact { display: flex; flex-direction: column; }
  .contact__name { color: var(--cyan); font-weight: 700; font-size: 22px; line-height: 1.1; }
  .contact__role { color: var(--ink-soft); font-size: 12px; font-weight: 500; margin: 4px 0 10px; letter-spacing: .3px; }
  .contact__line {
    display: flex; align-items: center; gap: 7px;
    color: var(--ink); font-size: 11.5px; font-weight: 500; line-height: 1.75; letter-spacing: .2px;
  }
  .contact__icon { width: 11px; height: 11px; flex: none; }
  .accent { color: var(--cyan); }
</style>
</head>
<body>
<main class="stage">
  <section class="card card--front" aria-label="Card front">
    <div class="brand"><span class="brand__dot"></span>BrivoMatex</div>
  </section>

  <section class="card card--back" aria-label="Card back">
    <div class="brand"><span class="brand__dot"></span>BrivoMatex</div>
    <div class="divider"></div>
    <div class="contact">
      <p class="contact__name">Tommaso Ferlini</p>
      <p class="contact__role">CEO &amp; Founder</p>
      <p class="contact__line">
        <svg class="contact__icon" viewBox="0 0 24 24" fill="var(--cyan)"><path d="M6.6 10.8a15.1 15.1 0 0 0 6.6 6.6l2.2-2.2a1 1 0 0 1 1-.25 11.4 11.4 0 0 0 3.6.57 1 1 0 0 1 1 1V20a1 1 0 0 1-1 1A17 17 0 0 1 3 4a1 1 0 0 1 1-1h3.5a1 1 0 0 1 1 1c0 1.25.2 2.45.57 3.57a1 1 0 0 1-.25 1z"/></svg>
        +34 611.205.938
      </p>
      <p class="contact__line">
        <svg class="contact__icon" viewBox="0 0 24 24" fill="none" stroke="var(--cyan)" stroke-width="2.2"><rect x="2.5" y="5" width="19" height="14" rx="1.5"/><path d="M3 6l9 7 9-7"/></svg>
        tommaso.ferlini@brivomatex.example
      </p>
      <p class="contact__line">
        <svg class="contact__icon" viewBox="0 0 24 24" fill="none" stroke="var(--cyan)" stroke-width="2"><circle cx="12" cy="12" r="9.5"/><path d="M2.5 12h19M12 2.5c3 3.2 3 15.8 0 19M12 2.5c-3 3.2-3 15.8 0 19"/></svg>
        <span>www.<span class="accent">brivomatex</span>.example</span>
      </p>
    </div>
  </section>
</main>
</body>
</html>
```